Harbor Sushi & Steak Dinner Menu

I'm looking for a MENU design with a particular feel. I want to have a base template made that I can then use for future alterations to the menu; ie I can go in and change out different entrees as the menu changes but the template will remain the same. (Ideally it would be in an Apple Pages format.). Also ideally - dinner menu will occupy 2 pages 8.5 x 11. The restaurant's name is Harbor. It is a MODERN steak house that will also feature Sushi, a Raw Bar, Exquisite Cocktails and a sophisticated nightlife crowd. I have attached our LOGO, a secondary logo that we will be featuring throughout the project including on the menu cover (the gold U). Finally - I have attached the content that we would like to see. AGAIN - I REITERATE: High end dining and lounge atmosphere. A couple of restaurants / menus that I love are Morvendel in NYC and Pellucid Steakhouse in Long Island NY. Please do not duplicate - just trying to offer some suggestions.

Requirements
Must have
• A sophisticated and elegant feel without being stuffy or old.

```html
<!DOCTYPE html>
<html lang="en">
<head>
<meta charset="utf-8">
<title>Harbor Sushi &amp; Steak — Dinner Menu</title>
<link href="https://fonts.googleapis.com/css2?family=Josefin+Sans:wght@600;700&family=Montserrat:wght@400;600;700;800&display=swap" rel="stylesheet">
<style>
  :root{
    --board:#808080;
    --ink-black:#000;
    --paper:#fff;
    --red:#d1212f;
    --gold:#cdb779;
    --gold-dark:#b99a5c;
    --copper:#b8775a;
    --body-light:#c9c9c9;
    --body-dark:#5a5a5a;
    --label:#fff;
  }
  *{margin:0;padding:0;box-sizing:border-box}
  html,body{width:1200px;height:3979px;overflow:hidden}
  body{background:var(--board);position:relative;font-family:"Montserrat",sans-serif}

  .board-label{
    position:absolute;left:60px;
    writing-mode:vertical-rl;transform:rotate(180deg);
    font-family:"Montserrat",sans-serif;font-weight:700;
    font-size:64px;letter-spacing:1px;color:var(--label);line-height:1;
  }

  .panel{position:absolute;left:136px;width:927px;height:1199px;overflow:hidden}
  .panel--cover{top:131px;background:radial-gradient(circle at 50% 45%,#5a1016 0%,#2c0709 28%,#0a0102 50%,#000 70%)}
  .panel--dark{top:1387px;background:var(--ink-black)}
  .panel--light{top:2642px;background:var(--paper)}

  /* Cover */
  .cover-seal{
    position:absolute;left:352px;top:430px;width:222px;height:222px;border-radius:50%;
    background:#050505;display:flex;align-items:center;justify-content:center;
  }
  .cover-name{font-family:"Josefin Sans",sans-serif;font-weight:700;font-size:58px;letter-spacing:8px;color:var(--gold);padding-left:8px;padding-top:8px}
  .cover-title{position:absolute;left:0;right:0;text-align:center;font-family:"Josefin Sans",sans-serif;font-weight:700}
  .cover-title--kicker{top:1008px;font-size:25px;letter-spacing:13px;color:var(--red)}
  .cover-title--main{top:1040px;font-size:38px;letter-spacing:7px;color:var(--gold)}

  /* Ribbon */
  .ribbon{position:absolute;left:710px;top:0;width:102px;height:176px}
  .ribbon-name{position:absolute;left:710px;top:72px;width:102px;text-align:center;font-family:"Josefin Sans",sans-serif;font-weight:700;font-size:17px;letter-spacing:2px;color:#2a1a10}

  /* Menu */
  .menu-section{position:absolute;left:82px;width:800px}
  .menu-heading{font-family:"Josefin Sans",sans-serif;font-weight:700;font-size:26px;letter-spacing:4.5px;color:var(--red);line-height:26px;height:26px;margin-bottom:6px;white-space:nowrap}
  .menu-item{display:block;font-size:14px;line-height:22px;height:22px;white-space:nowrap;overflow:visible}
  .menu-item--wrap{height:41px}
  .menu-item--note{line-height:14px;height:14px;margin-bottom:4px}
  .menu-item b{font-weight:700}
  .menu-item .cont{display:block;padding-left:63px;line-height:16px;height:16px;margin-bottom:3px}
  .menu-item .cont--wide{padding-left:219px}
  .gf{font-size:6px;line-height:1;font-weight:700;vertical-align:baseline;margin-left:3px;letter-spacing:0}

  .panel--dark .menu-item{color:var(--body-light)}
  .panel--dark .menu-item b{color:var(--gold)}
  .panel--light .menu-item{color:var(--body-dark)}
  .panel--light .menu-item b{color:var(--gold-dark);font-weight:600}
</style>
</head>
<body>

<div class="board-label" style="top:131px">COVER</div>
<div class="board-label" style="top:1387px">INSIDE-OPTION 1</div>
<div class="board-label" style="top:2642px">INSIDE-OPTION 2</div>

<section class="panel panel--cover">
  <div class="cover-seal"><span class="cover-name">HARBOR</span></div>
  <div class="cover-title cover-title--kicker">SUSHI &amp; STEAK</div>
  <div class="cover-title cover-title--main">DINNER MENU</div>
</section>

<section class="panel panel--dark">
  <svg class="ribbon" viewBox="0 0 102 176" aria-hidden="true">
    <defs><linearGradient id="ribbon-fill-a" x1="0" y1="0" x2="0" y2="1"><stop offset="0" stop-color="#d7c890"/><stop offset="1" stop-color="#b8775a"/></linearGradient></defs>
    <polygon points="0,0 102,0 102,176 51,150 0,176" fill="url(#ribbon-fill-a)"/>
  </svg>
  <div class="ribbon-name">HARBOR</div>

  <div class="menu-section" style="top:84px">
    <h2 class="menu-heading">SUSHI / SASHIMI</h2>
    <p class="menu-item"><b>TORO:</b> blue fin tuna belly<span class="gf">GF</span></p>
    <p class="menu-item"><b>EBI:</b> cooked shrimp<span class="gf">GF</span></p>
    <p class="menu-item"><b>HAMACHI:</b> yellowtail<span class="gf">GF</span></p>
    <p class="menu-item"><b>UNI:</b> sea urchin<span class="gf">GF</span></p>
    <p class="menu-item"><b>HIRAME:</b> fluke<span class="gf">GF</span></p>
    <p class="menu-item"><b>UNAGI:</b> fresh water eel<span class="gf">GF</span></p>
    <p class="menu-item"><b>SAKE:</b> salmon<span class="gf">GF</span></p>
    <p class="menu-item"><b>MADAI:</b> red snapper<span class="gf">GF</span></p>
    <p class="menu-item"><b>MAGURO:</b> tuna<span class="gf">GF</span></p>
  </div>
  <div class="menu-section" style="top:328px">
    <h2 class="menu-heading">SUSHI PLATTERS</h2>
    <p class="menu-item"><b>SMALL:</b> Five Pieces assorted sushi, nine pieces sashimi, spicy tuna roll<span class="gf">GF</span></p>
    <p class="menu-item menu-item--wrap"><b>LARGE:</b> Eight Pieces assorted sushi, eighteen pieces of sashimi, alaskan roll,<span class="cont">rainbow roll<span class="gf">GF</span></span></p>
  </div>
  <div class="menu-section" style="top:435px">
    <h2 class="menu-heading">CLASSIC ROLLS</h2>
    <p class="menu-item"><b>YELLOWTAIL:</b> inside out roll with scallions<span class="gf">GF</span></p>
    <p class="menu-item menu-item--note">Spicy Tuna or Salmon or Yellowtail; spicy mayo</p>
    <p class="menu-item"><b>CALIFORNIA:</b> crab meat, cucumber and avocado<span class="gf">GF</span></p>
    <p class="menu-item"><b>VEGETABLE:</b> avocado, cucumber, asparagus and pickled reddish<span class="gf">GF</span></p>
    <p class="menu-item"><b>SPIDER:</b> soft shell crab and avocado with eel sauce</p>
    <p class="menu-item"><b>SHRIMP TEMPURA:</b> deep fried tempura shrimp and eel sauce</p>
    <p class="menu-item"><b>ALASKAN:</b> salmon and avocado<span class="gf">GF</span></p>
  </div>
  <div class="menu-section" style="top:629px">
    <h2 class="menu-heading">SPECIAL ROLLS</h2>
    <p class="menu-item"><b>THE HARBOR:</b> tuna, salmon, yellowtail, avocado, spicy mayo, soy bean paper</p>
    <p class="menu-item"><b>KING CRAB RAINBOW:</b> king crab, avocado, cucumbers, assorted fish on top</p>
    <p class="menu-item"><b>EMPRESS:</b> Shrimp tempura, spicy tuna on top, eel sauce, spicy mayo</p>
    <p class="menu-item"><b>SPICY GIRL:</b> Spicy crunchy crab meat, cucumber, shrimp on top</p>
    <p class="menu-item"><b>DRAGON:</b> Eel, cucumber, avocado, and tobiko on top, eel sauce</p>
    <p class="menu-item"><b>YUMMY:</b> spicy crunchy salmon, avocado, mango and salmon on top</p>
    <p class="menu-item"><b>NO. 9:</b> Shrimp Tempura, avocado, kani, spicy mayo, tobiko</p>
    <p class="menu-item"><b>SUNRISE ROLL:</b> spicy crunchy tuna and avocado, spicy crunchy salmon on top</p>
  </div>
  <div class="menu-section" style="top:852px">
    <h2 class="menu-heading">SEAFOOD RAW BAR</h2>
    <p class="menu-item"><b>LOBSTER COCKTAIL</b></p>
    <p class="menu-item"><b>SHRIMP COCKTAIL</b></p>
    <p class="menu-item"><b>CLAMS ON THE HALF SHELL</b></p>
    <p class="menu-item"><b>OYSTERS ON THE HALF SHELL</b></p>
    <p class="menu-item"><b>COLOSSAL CRAB COCKTAIL</b></p>
    <p class="menu-item menu-item--wrap"><b>RAW BAR PLATE FOR ONE:</b> Two Shrimp, Half of a One Pound Lobster,<span class="cont cont--wide">Two Clams, One East Coast Oyster, One West Coast Oyster</span></p>
  </div>
  <div class="menu-section" style="top:1046px">
    <h2 class="menu-heading">SEAFOOD PLATTERS<span class="gf">GF</span></h2>
    <p class="menu-item">Shrimp, Oysters, Clams, Lobster and Crab</p>
    <p class="menu-item"><b>LARGE OR COLOSSAL</b></p>
  </div>
</section>

<section class="panel panel--light">
  <svg class="ribbon" viewBox="0 0 102 176" aria-hidden="true">
    <defs><linearGradient id="ribbon-fill-b" x1="0" y1="0" x2="0" y2="1"><stop offset="0" stop-color="#d7c890"/><stop offset="1" stop-color="#b8775a"/></linearGradient></defs>
    <polygon points="0,0 102,0 102,176 51,150 0,176" fill="url(#ribbon-fill-b)"/>
  </svg>
  <div class="ribbon-name">HARBOR</div>

  <div class="menu-section" style="top:84px">
    <h2 class="menu-heading">SUSHI / SASHIMI</h2>
    <p class="menu-item"><b>TORO:</b> blue fin tuna belly<span class="gf">GF</span></p>
    <p class="menu-item"><b>EBI:</b> cooked shrimp<span class="gf">GF</span></p>
    <p class="menu-item"><b>HAMACHI:</b> yellowtail<span class="gf">GF</span></p>
    <p class="menu-item"><b>UNI:</b> sea urchin<span class="gf">GF</span></p>
    <p class="menu-item"><b>HIRAME:</b> fluke<span class="gf">GF</span></p>
    <p class="menu-item"><b>UNAGI:</b> fresh water eel<span class="gf">GF</span></p>
    <p class="menu-item"><b>SAKE:</b> salmon<span class="gf">GF</span></p>
    <p class="menu-item"><b>MADAI:</b> red snapper<span class="gf">GF</span></p>
    <p class="menu-item"><b>MAGURO:</b> tuna<span class="gf">GF</span></p>
  </div>
  <div class="menu-section" style="top:328px">
    <h2 class="menu-heading">SUSHI PLATTERS</h2>
    <p class="menu-item"><b>SMALL:</b> Five Pieces assorted sushi, nine pieces sashimi, spicy tuna roll<span class="gf">GF</span></p>
    <p class="menu-item menu-item--wrap"><b>LARGE:</b> Eight Pieces assorted sushi, eighteen pieces of sashimi, alaskan roll,<span class="cont">rainbow roll<span class="gf">GF</span></span></p>
  </div>
  <div class="menu-section" style="top:435px">
    <h2 class="menu-heading">CLASSIC ROLLS</h2>
    <p class="menu-item"><b>YELLOWTAIL:</b> inside out roll with scallions<span class="gf">GF</span></p>
    <p class="menu-item menu-item--note">Spicy Tuna or Salmon or Yellowtail; spicy mayo</p>
    <p class="menu-item"><b>CALIFORNIA:</b> crab meat, cucumber and avocado<span class="gf">GF</span></p>
    <p class="menu-item"><b>VEGETABLE:</b> avocado, cucumber, asparagus and pickled reddish<span class="gf">GF</span></p>
    <p class="menu-item"><b>SPIDER:</b> soft shell crab and avocado with eel sauce</p>
    <p class="menu-item"><b>SHRIMP TEMPURA:</b> deep fried tempura shrimp and eel sauce</p>
    <p class="menu-item"><b>ALASKAN:</b> salmon and avocado<span class="gf">GF</span></p>
  </div>
  <div class="menu-section" style="top:629px">
    <h2 class="menu-heading">SPECIAL ROLLS</h2>
    <p class="menu-item"><b>THE HARBOR:</b> tuna, salmon, yellowtail, avocado, spicy mayo, soy bean paper</p>
    <p class="menu-item"><b>KING CRAB RAINBOW:</b> king crab, avocado, cucumbers, assorted fish on top</p>
    <p class="menu-item"><b>EMPRESS:</b> Shrimp tempura, spicy tuna on top, eel sauce, spicy mayo</p>
    <p class="menu-item"><b>SPICY GIRL:</b> Spicy crunchy crab meat, cucumber, shrimp on top</p>
    <p class="menu-item"><b>DRAGON:</b> Eel, cucumber, avocado, and tobiko on top, eel sauce</p>
    <p class="menu-item"><b>YUMMY:</b> spicy crunchy salmon, avocado, mango and salmon on top</p>
    <p class="menu-item"><b>NO. 9:</b> Shrimp Tempura, avocado, kani, spicy mayo, tobiko</p>
    <p class="menu-item"><b>SUNRISE ROLL:</b> spicy crunchy tuna and avocado, spicy crunchy salmon on top</p>
  </div>
  <div class="menu-section" style="top:852px">
    <h2 class="menu-heading">SEAFOOD RAW BAR</h2>
    <p class="menu-item"><b>LOBSTER COCKTAIL</b></p>
    <p class="menu-item"><b>SHRIMP COCKTAIL</b></p>
    <p class="menu-item"><b>CLAMS ON THE HALF SHELL</b></p>
    <p class="menu-item"><b>OYSTERS ON THE HALF SHELL</b></p>
    <p class="menu-item"><b>COLOSSAL CRAB COCKTAIL</b></p>
    <p class="menu-item menu-item--wrap"><b>RAW BAR PLATE FOR ONE:</b> Two Shrimp, Half of a One Pound Lobster,<span class="cont cont--wide">Two Clams, One East Coast Oyster, One West Coast Oyster</span></p>
  </div>
  <div class="menu-section" style="top:1046px">
    <h2 class="menu-heading">SEAFOOD PLATTERS<span class="gf">GF</span></h2>
    <p class="menu-item">Shrimp, Oysters, Clams, Lobster and Crab</p>
    <p class="menu-item"><b>LARGE OR COLOSSAL</b></p>
  </div>
</section>

</body>
</html>
```